Medical Call Centre Needs a Web Design

We need a web design for a new company based in Melbourne called "Clinora Services". We provide medical centres with administrative support by managing inbound calls to our clients facility. We require a clean, simple and easy to navigate website with an ultimate end product alike this - http://www.plumevanta.com/

The final design should communicate professionalism, new age and inovative.

Industry/Entity Type

It Company

```html
<!DOCTYPE html>
<html lang="en">
<head>
<meta charset="utf-8">
<title>Clinora Services</title>
<link href="https://fonts.googleapis.com/css2?family=Roboto:wght@400;500;700;900&family=Roboto+Condensed:wght@700&display=swap" rel="stylesheet">
<style>
:root{
  --yellow:#f2b92a;
  --yellow-light:#f7cd3e;
  --red:#e3483c;
  --red-dark:#d93b33;
  --dark:#3c3c3c;
  --dark-deep:#2e2e2e;
  --white:#ffffff;
  --cream:#fde9b0;
}
*{margin:0;padding:0;box-sizing:border-box}
html,body{width:1200px;height:4839px;overflow:hidden}
body{font-family:"Roboto",Arial,sans-serif;color:var(--white);position:relative;background:var(--dark)}
section,header,footer{position:absolute;left:0;width:1200px}
.abs{position:absolute}
.center{left:0;width:1200px;text-align:center}
.section-title{font-family:"Roboto Condensed","Roboto",sans-serif;font-weight:700;font-size:44px;letter-spacing:1px}
.section-sub{font-size:14px;opacity:.85}
.btn{position:absolute;border:2px solid var(--white);color:var(--white);font-size:13px;font-weight:700;display:flex;align-items:center;justify-content:center;letter-spacing:.5px}
.para{font-size:12.5px;line-height:22px}

/* hero */
.hero{top:0;height:587px;background:radial-gradient(ellipse at 65% 55%,var(--yellow-light),var(--yellow) 60%,#eaa820)}
.brand{left:175px;top:14px;font-size:30px;font-weight:700;line-height:32px;width:150px}
.nav{left:410px;top:36px;display:flex}
.nav a{font-size:12px;font-weight:500;color:var(--white);text-decoration:none;padding:6px 20px;letter-spacing:.4px}
.nav a.active{border:2px solid var(--white);padding:4px 18px}
.hero-kicker{top:205px;font-family:"Roboto Condensed","Roboto",sans-serif;font-weight:700;font-size:42px}
.hero-main{top:252px;font-family:"Roboto Condensed","Roboto",sans-serif;font-weight:700;font-size:58px}
.hero-rule{left:440px;top:334px;width:320px;height:3px;background:var(--white)}
.hero-tag{top:360px;font-family:"Roboto Condensed","Roboto",sans-serif;font-weight:700;font-size:42px}
.arrow{top:262px;width:20px;height:70px}

/* about */
.about{top:587px;height:749px;background:linear-gradient(160deg,var(--red),var(--red-dark))}
.about-emblem{left:39px;top:171px;width:381px;height:387px;background:radial-gradient(ellipse at center,rgba(255,255,255,.9) 0,rgba(255,255,255,.55) 45%,rgba(255,255,255,0) 72%)}
.about-title{left:500px;top:170px;font-family:"Roboto Condensed","Roboto",sans-serif;font-weight:700;font-size:46px;line-height:54px}
.about-lead{left:500px;top:298px;font-size:15px}
.about-text{left:500px;top:348px;width:590px}

/* services */
.services{top:1336px;height:871px;background:linear-gradient(180deg,#474747,var(--dark) 50%,var(--dark-deep))}
.svc{position:absolute;width:371px;height:133px;border:2px solid rgba(255,255,255,.75);background:rgba(0,0,0,.08)}
.svc-icon{position:absolute;left:24px;top:30px;width:56px;height:56px;border:2px solid var(--white)}
.svc-name{position:absolute;left:108px;top:26px;font-size:14px;font-weight:700}
.svc-text{position:absolute;left:108px;top:50px;width:230px;font-size:11px;line-height:17px}
.timeline{left:596px;top:267px;width:2px;height:462px;background:rgba(255,255,255,.8)}
.dot{position:absolute;width:14px;height:14px;border:2px solid var(--white);border-radius:50%;background:var(--dark);left:590px}

/* blog */
.blog{top:2207px;height:884px;background:radial-gradient(ellipse at 55% 45%,var(--yellow-light),var(--yellow) 65%,#e9a722)}
.blog-visual{left:123px;top:251px;width:309px;height:471px;background:linear-gradient(160deg,rgba(255,255,255,.85),rgba(255,255,255,.55))}
.blog-head{left:510px;top:292px;width:560px;font-family:"Roboto Condensed","Roboto",sans-serif;font-weight:700;font-size:21px;line-height:27px}
.blog-text{left:510px;top:370px;width:560px;color:var(--cream)}
.blog-date{left:510px;top:552px;font-size:12px;font-weight:500;color:var(--cream)}

/* testimonials */
.testimonials{top:3091px;height:871px;background:linear-gradient(160deg,var(--red),var(--red-dark))}
.portrait{left:371px;top:280px;width:155px;height:152px;border:4px solid var(--white);background:linear-gradient(160deg,#e8dcd2,#c9b7a8)}
.quote-head{left:150px;top:480px;width:600px;text-align:center;font-family:"Roboto Condensed","Roboto",sans-serif;font-weight:700;font-size:17px;line-height:30px}
.quote-text{left:200px;top:552px;width:500px;text-align:center}
.quote-name{left:150px;top:646px;width:600px;text-align:center;font-size:12px;font-weight:700}
.pager{left:410px;top:686px;display:flex;gap:5px}
.pager span{width:11px;height:11px;border:1px solid var(--white)}
.pager span.on{background:var(--white)}
.testimonial-visual{left:790px;top:354px;width:310px;height:325px;background:linear-gradient(160deg,rgba(255,255,255,.8),rgba(255,255,255,.5))}

/* contact */
.contact{top:3962px;height:877px;background:linear-gradient(180deg,#444,var(--dark) 60%,var(--dark-deep))}
.info-label{font-size:14px;font-weight:700}
.info-text{font-size:13px;line-height:20px;margin-top:10px;opacity:.9}
.copyright{left:174px;top:526px;font-size:11px;opacity:.85}
.social{left:784px;top:524px;display:flex;gap:14px}
.social span{width:14px;height:14px;background:var(--white);opacity:.85}
</style>
</head>
<body>

<header class="hero">
  <div class="abs brand">Clinora Services</div>
  <nav class="abs nav">
    <a class="active">HOME</a><a>ABOUT US</a><a>SERVICES</a><a>BLOG</a><a>TESTIMONIALS</a><a>CONTACT US</a>
  </nav>
  <svg class="abs arrow" style="left:64px" viewBox="0 0 20 70"><path d="M18 2 L3 35 L18 68" fill="none" stroke="#fff" stroke-width="2" opacity=".7"/></svg>
  <svg class="abs arrow" style="left:1112px" viewBox="0 0 20 70"><path d="M2 2 L17 35 L2 68" fill="none" stroke="#fff" stroke-width="2" opacity=".7"/></svg>
  <h1 class="abs center hero-kicker">WE PROVIDE</h1>
  <div class="abs center hero-main">MEDICAL CENTRES</div>
  <div class="abs hero-rule"></div>
  <div class="abs center hero-tag">WITH ADMINISTRATIVE SUPPORT</div>
</header>

<section class="about">
  <div class="abs about-emblem" role="img" aria-label="Large white medical staff emblem"></div>
  <h2 class="abs about-title">ABOUT<br>CLINORA SERVICES</h2>
  <p class="abs about-lead">It is a long established fact that a reader will be distracted by the readable</p>
  <p class="abs para about-text">It is a long established fact that a reader will be distracted by the readable content of a page when looking at its layout. The point of using Lorem Ipsum is that it has a more-or-less normal distribution of letters, as opposed to using 'Content here, content here', making it look like readable English. Many desktop publishing packages and web page editors now use Lorem Ipsum as their default model text, and a search for 'lorem ipsum' will uncover many web sites still in their infancy. Various versions have evolved over the years, sometimes by accident, sometimes on purpose.</p>
  <div class="btn" style="left:500px;top:555px;width:184px;height:39px">VIEW ALL SERVICES</div>
</section>

<section class="services">
  <h2 class="abs center section-title" style="top:62px">SERVICES</h2>
  <p class="abs center section-sub" style="top:140px">It is a long established fact that a reader will be distracted by the readable</p>
  <div class="abs timeline"></div>
  <div class="dot" style="top:261px"></div>
  <div class="dot" style="top:443px"></div>
  <div class="dot" style="top:617px"></div>

  <div class="svc" style="left:155px;top:206px">
    <svg class="svc-icon" viewBox="0 0 56 56"><circle cx="24" cy="26" r="9" fill="none" stroke="#fff" stroke-width="2"/><path d="M24 35 v6 h12 v-10" fill="none" stroke="#fff" stroke-width="2"/><circle cx="36" cy="28" r="3" fill="#fff"/></svg>
    <div class="svc-name">SERVICES - 01</div>
    <div class="svc-text">It is a long established fact that a reader will be distracted by the readable content of a page when looking at its layout.</div>
  </div>
  <div class="svc" style="left:671px;top:384px">
    <svg class="svc-icon" viewBox="0 0 56 56"><path d="M28 40 C14 30 16 18 23 18 C26 18 28 21 28 21 C28 21 30 18 33 18 C40 18 42 30 28 40Z" fill="#fff"/></svg>
    <div class="svc-name">SERVICES - 02</div>
    <div class="svc-text">It is a long established fact that a reader will be distracted by the readable content of a page when looking at its layout.</div>
  </div>
  <div class="svc" style="left:155px;top:564px">
    <svg class="svc-icon" viewBox="0 0 56 56"><rect x="15" y="20" width="26" height="20" fill="#fff"/><rect x="23" y="15" width="10" height="6" fill="none" stroke="#fff" stroke-width="2"/><path d="M28 24 v12 M22 30 h12" stroke="#3c3c3c" stroke-width="3"/></svg>
    <div class="svc-name">SERVICES - 03</div>
    <div class="svc-text">It is a long established fact that a reader will be distracted by the readable content of a page when looking at its layout.</div>
  </div>
  <div class="btn" style="left:500px;top:735px;width:184px;height:37px">VIEW ALL SERVICES</div>
</section>

<section class="blog">
  <h2 class="abs center section-title" style="top:96px">BLOG</h2>
  <p class="abs center section-sub" style="top:176px">It is a long established fact that a reader will be distracted by the readable</p>
  <div class="abs blog-visual" role="img" aria-label="Illustration of a white tablet showing speech bubbles"></div>
  <h3 class="abs blog-head">IT IS A LONG ESTABLISHED FACT THAT A<br>READER WILL BE DISTRACTED BY THE READABLE</h3>
  <p class="abs para blog-text">It is a long established fact that a reader will be distracted by the readable content of a page when looking at its layout. The point of using Lorem Ipsum is that it has a more-or-less normal distribution of letters, as opposed to using 'Content here, content here', making it look like readable English. Many desktop publishing packages and web page editors now use Lorem Ipsum as their default model text, and a search for 'lorem ipsum' will uncover many web sites still in their infancy. Various versions have evolved over the years, sometimes by accident, sometimes on purpose.</p>
  <div class="abs blog-date">- POSTED ON 17 MARCH 2014 -</div>
  <div class="btn" style="left:510px;top:596px;width:184px;height:39px">VIEW ALL POSTS</div>
</section>

<section class="testimonials">
  <h2 class="abs section-title" style="left:276px;top:108px">TESTIMONIALS</h2>
  <p class="abs section-sub" style="left:200px;top:182px">It is a long established fact that a reader will be distracted by the readable</p>
  <div class="abs portrait" role="img" aria-label="Portrait photo of a client"></div>
  <h3 class="abs quote-head">IT IS A LONG ESTABLISHED FACT THAT A<br>READER WILL BE DISTRACTED BY THE READABLE</h3>
  <p class="abs para quote-text">It is a long established fact that a reader will be distracted by the readable content of a page when looking at its layout. The point of using Lorem Ipsum is that it has a more-or-less normal distribution of letters, as opposed to using 'Content here.</p>
  <div class="abs quote-name">- MARLA QUINT -</div>
  <div class="abs pager"><span class="on"></span><span></span><span></span><span></span><span></span></div>
  <div class="btn" style="left:358px;top:741px;width:184px;height:37px">VIEW ALL POSTS</div>
  <div class="abs testimonial-visual" role="img" aria-label="Large white illustration of a pencil writing in a box"></div>
</section>

<footer class="contact">
  <h2 class="abs center section-title" style="top:176px">GET IN TOUCH</h2>
  <p class="abs center section-sub" style="top:256px">It is a long established fact that a reader will be distracted by the readable</p>

  <svg class="abs" style="left:172px;top:382px" width="34" height="34" viewBox="0 0 24 24"><path d="M6.6 10.8c1.4 2.8 3.8 5.1 6.6 6.6l2.2-2.2c.3-.3.7-.4 1-.2 1.1.4 2.3.6 3.6.6.6 0 1 .4 1 1V20c0 .6-.4 1-1 1C10.6 21 3 13.4 3 4c0-.6.4-1 1-1h3.5c.6 0 1 .4 1 1 0 1.3.2 2.5.6 3.6.1.3 0 .7-.2 1L6.6 10.8z" fill="#fff"/></svg>
  <div class="abs" style="left:232px;top:380px"><div class="info-label">PHONES</div><div class="info-text">+1 555 014 2102<br>+1 555 014 2103</div></div>

  <svg class="abs" style="left:468px;top:380px" width="26" height="38" viewBox="0 0 24 34"><path d="M12 0C5.4 0 0 5.4 0 12c0 9 12 22 12 22s12-13 12-22C24 5.4 18.6 0 12 0zm0 17a5 5 0 1 1 0-10 5 5 0 0 1 0 10z" fill="#fff"/></svg>
  <div class="abs" style="left:523px;top:380px"><div class="info-label">OFFICE ADDRESS</div><div class="info-text">4 Clinora Services<br>3rd Floor<br>State, 1000,<br>Country</div></div>

  <svg class="abs" style="left:782px;top:385px" width="42" height="30" viewBox="0 0 42 30"><rect width="42" height="30" fill="#fff"/><path d="M1 1 L21 17 L41 1" fill="none" stroke="#3c3c3c" stroke-width="3"/></svg>
  <div class="abs" style="left:848px;top:380px"><div class="info-label">EMAILS</div><div class="info-text">hello@clinora.example<br>sales@clinora.example</div></div>

  <div class="abs copyright">Copyright © 2014 Clinora Services . All rights reserved</div>
  <div class="abs social"><span></span><span></span><span></span><span></span><span></span><span></span><span></span><span></span><span></span><span></span></div>
  <svg class="abs" style="left:1122px;top:522px" width="18" height="18" viewBox="0 0 18 18"><path d="M3 12 L9 5 L15 12" fill="none" stroke="#fff" stroke-width="2"/></svg>
</footer>

</body>
</html>
```